In-product message pop-up (to upsell software users to paid WHILE using software)

We need an IRRESISTIBLY CLICKABLE pop-up window to present to Windows desktop users of our software security suite. The pop-up will be presented to active users of Korvel's Trailmute software with the ultimate goal of UPSELLING them to buy Korvel's premium product called "VaultSweep" which helps users to scan and remove their data from the darkweb. https://www.korvelsoft.example/en-us/vaultsweep Some FAILED pop-ups are attached as images. The words of these pop-ups are fine, but we need 5X better results than these tests. Please STUDY what the team has ALREADY tried, and think of a message and design that is MORE COMPELLING for users of an anti-track software to CLICK ON in regards to protecting themselves from compromised email/passwords/personal information being leaked by hackers. You only have room for a few words and 1-2 sentences. Think! The best design that will maximize clicks while complying with the corporate style of Korvelsoft.example will win!

Target Market(s)

U.S. users of VPN and anti-track/anti-cookie software

Industry/Entity Type

Computer Software

Font styles to use
Sans Serif

Requirements
Must have
• Acceptable sizes: 728X90, 300X250, or 300X600. Follow the color scheme of Korvel. https://www.korvelsoft.example/en-us/about The message must
Nice to have
• Follow the corporate look n' feel of Korvel. But think CREATIVELY about how to convince someone who is using Korvel's free software to CLICK on the pop-up while they're using their desktop and LEARN about VaultSweep https://findlumen.example/?q=korvel&t=osx&iax=images&ia=images Again we are advertising "VaultSweep" which helps users to remove their personal data from the darkweb and prevent data breaches. But your pop-up shouldn't reference VaultSweep specifically, it should just maximize clicks about something that appeals to the user, in a way that relates to VaultSweep's value proposition (protect yourself, remove your data, scan your email, resolve security concerns, etc.)
Should not have
• Nothing that Korvel corporate won't approve (pornography, profanity, risqué photos, sensational language, etc.)

```html
<!DOCTYPE html>
<html lang="en">
<head>
<meta charset="utf-8">
<title>Korvel – Data removal pop-up</title>
<link rel="stylesheet" href="https://fonts.googleapis.com/css2?family=Open+Sans:wght@400;600&display=swap">
<style>
  :root {
    --navy-deep: #15123f;
    --navy-mid: #221f5c;
    --navy-soft: #2b2a72;
    --wave: #1d1a4e;
    --ice-light: #4a48ff;
    --ice-dark: #2b2aa6;
    --badge: #6a63b3;
    --text: #ffffff;
    --close: #8a89a8;
    --cta: #4bb55a;
    --footer: #2e3547;
    --brand-dot: #ff7a1a;
  }
  * { margin: 0; padding: 0; box-sizing: border-box; }
  html, body {
    width: 1200px;
    height: 2398px;
    overflow: hidden;
    background: var(--navy-deep);
  }
  .popup {
    position: relative;
    width: 1200px;
    height: 2398px;
    overflow: hidden;
    font-family: "Open Sans", sans-serif;
    color: var(--text);
    background: linear-gradient(180deg, var(--navy-deep) 0%, var(--navy-mid) 40%, var(--navy-soft) 100%);
  }
  .popup__wave {
    position: absolute;
    inset: 0;
    width: 1200px;
    height: 2398px;
  }
  .brand {
    position: absolute;
    left: 60px;
    top: 66px;
    display: flex;
    align-items: center;
    gap: 16px;
    font-size: 60px;
    font-weight: 600;
    letter-spacing: -1px;
    line-height: 1;
  }
  .brand__dot {
    width: 56px;
    height: 56px;
    border-radius: 50%;
    background: var(--brand-dot);
  }
  .close-button {
    position: absolute;
    right: 40px;
    top: 66px;
    width: 48px;
    height: 48px;
  }
  .hero-art {
    position: absolute;
    left: 527px;
    top: 211px;
    width: 673px;
    height: 993px;
    background: radial-gradient(ellipse at 45% 40%, var(--ice-light) 0%, var(--ice-dark) 45%, rgba(43, 42, 166, 0) 72%);
    opacity: 0.85;
  }
  .content {
    position: absolute;
    left: 111px;
    top: 1121px;
    width: 1050px;
  }
  .badge {
    display: inline-block;
    background: var(--badge);
    font-size: 33px;
    font-weight: 600;
    line-height: 75px;
    padding: 0 31px;
    border-radius: 3px;
  }
  .headline {
    margin-top: 62px;
    margin-left: 6px;
    font-size: 84px;
    font-weight: 400;
    line-height: 113px;
    letter-spacing: -0.5px;
  }
  .subline {
    margin-top: 54px;
    margin-left: 10px;
    font-size: 50px;
    font-weight: 400;
    line-height: 70px;
    white-space: nowrap;
  }
  .cta {
    display: inline-block;
    margin-top: 82px;
    width: 441px;
    height: 108px;
    background: var(--cta);
    border-radius: 3px;
    font-size: 36px;
    font-weight: 600;
    line-height: 108px;
    text-align: center;
    color: var(--text);
    text-decoration: none;
  }
  .footer-bar {
    position: absolute;
    left: 0;
    bottom: 0;
    width: 1200px;
    height: 105px;
    background: var(--footer);
  }
</style>
</head>
<body>
  <div class="popup">
    <svg class="popup__wave" viewBox="0 0 1200 2398" aria-hidden="true">
      <path d="M0 385 C 250 430, 600 420, 900 380 C 1050 360, 1150 360, 1200 375 L 1200 2398 L 0 2398 Z" fill="var(--wave)" opacity="0.55"/>
      <path d="M1200 1050 C 900 1250, 520 1600, 530 2100 L 540 2398 L 1200 2398 Z" fill="var(--wave)" opacity="0.5"/>
    </svg>

    <div class="brand">
      <span class="brand__dot" aria-hidden="true"></span>
      <span class="brand__name">Korvel</span>
    </div>

    <svg class="close-button" viewBox="0 0 48 48" aria-label="Close">
      <path d="M4 4 L44 44 M44 4 L4 44" stroke="var(--close)" stroke-width="6" stroke-linecap="round"/>
    </svg>

    <div class="hero-art" role="img" aria-label="Low-poly blue iceberg illustration, mostly hidden below the surface"></div>

    <div class="content">
      <span class="badge">NEW</span>
      <h1 class="headline">100+ companies may<br>be selling your<br>personal data online</h1>
      <p class="subline">Stop them with a data removal request</p>
      <a class="cta" href="#">REMOVE MY DATA</a>
    </div>

    <div class="footer-bar"></div>
  </div>
</body>
</html>
```